Modern Website For Law Firm Lawyer Melbourne, Australia Coded

We are looking for a modern and sophisticated website design. We would prefer the site to be based on WordPress given it is intuitive and some of our staff have experience using it.

Our law firm is based in Melbourne, Australia and we deal with property. The website must be hosted on a reliable Australian server.

We would also appreciate it if the designer can provide some guidance about how to make changes/upload content, such as photos and articles. We are happy to pay for this advice.

We prefer classic fonts in black or grey. We would also like a dash of colour so please use a green, blue or aqua colour palette that is consistent with our logo attached.

We do not want any law related images - scales of justice, gavel or the like.

Our ultimate goal is to communicate that the firm is professional, affordable, modern, dynamic, knowledgeable and one with the community.

We would like the following pages/sections/icons:

1. Who We Are - we will provide content.

2. Our Services - 1. Property 2. Wills, 3. Powers of Attorney 4. Probate & Estate Administration 5.Consultancy & Agency- we will provide content for each of these sections.

3. Articles - we already have approximately 20 articles on a wordpress blog and would like to port these articles to the website. We can do this ourselves if the designer can give us instructions about how to do this. We would also like to give clients the option to subscribe to our articles.

4. Contact Us - this should include our firms contact details; location map and we would like to give clients the option to "Request A Quote" directly from the page - i.e they will need to provide their full name, phone number email address, choose subject from drop down menu and type a message that gets sent to our outlook email.

5. Terms and Conditions - we will provide content

We really like the style and photographs used in the following website and want something as close to this as possible:

https://www.velbrook.com/

For privacy reasons, we would prefer to provide content together with all business details once we have decided on the winner.

We will monitor entries closely and promise to provide feedback and guidance on each entry.

This project is guaranteed. If our budget is too low please email us so we can discuss further and perhaps increase our budget. We are reasonable in this regard.

Thank you very much for considering this project.

Target Market(s)

General public, professionals, lawyers and conveyancers

Industry/Entity Type

Law Firm

Coding

Coded - Design and coding required

Number of Pages Required

1 page

Font styles to use
Sans Serif

Colors
33b8a4
33a6d7
0692cd
3176b5
00a990
9bcb3c
86cfc6
cadf82
85acd3

Requirements
Must have
• 1. Site must be coded and hosted on a reliable Australian server and it would be much appreciated if the deisgner provides instructions about how to add photos, blog articles etc-
• 2. The site must be secure and have green lock at top of page
• 3. Request A Quote - name, email, phone, drop down subject, message - email to our outlook email
• 4. Article Subscription
• 5. Domain (we have already purchased)
• 6. Location map
• 7. Facebook, LinkedIn, Instagram Icons
• 8. Membership icons in this order - KRT Member > Coastal Female Advocates > Guides From Counsel > Creature Foundation > Dorvo > Malpeth > Kel QR logos attached to go on bottom of page
• 9. Testimonials
Nice to have
• A modern, sophisticated website like:
• https://www.velbrook.com/ - we really like the style of the velbrook photographs
• We also really like this design by Tk of Sketch hive:
• https://www.sketchhive.com.au/design/58201346
Should not have
• Law related images - scales of justice gavel and the like

```html
<!DOCTYPE html>
<html lang="en">
<head>
<meta charset="utf-8">
<title>Ardmoor Legal</title>
<link rel="stylesheet" href="https://fonts.googleapis.com/css2?family=Raleway:wght@600;700;800&family=Open+Sans:ital,wght@0,400;0,600;0,700;1,400;1,600&display=swap">
<style>
:root{
  --teal:#2eadc0;
  --teal-dark:#2799ab;
  --ink:#2b2f36;
  --grey:#6f7378;
  --light:#f4f4f4;
  --line:#e4e4e4;
  --btn:#343c48;
  --navy:#262e3b;
  --white:#ffffff;
}
*{box-sizing:border-box;margin:0;padding:0}
html,body{width:1200px;height:3321px;overflow:hidden}
body{font-family:"Open Sans",Arial,sans-serif;color:var(--ink);background:var(--white);position:relative}
.page{position:relative;width:1200px;height:3321px}
section,header,footer,.topbar{position:absolute;left:0;width:1200px}
.abs{position:absolute}
.center{text-align:center;left:0;width:1200px}

/* top bar */
.topbar{top:0;height:36px;background:#fff;border-top:4px solid #34414f;border-bottom:1px solid var(--line)}
.topbar .note{position:absolute;left:157px;top:10px;font-size:9px;color:var(--grey)}
.social{position:absolute;display:flex;gap:6px}
.social span{display:block;width:18px;height:18px;background:var(--teal);border-radius:2px}
.topbar .social{right:157px;top:8px}

/* nav */
.nav{top:36px;height:72px;background:#fff;border-bottom:1px solid var(--line)}
.brand{position:absolute;left:157px;top:27px;font-family:"Open Sans",sans-serif;font-weight:700;font-size:14px;line-height:18px;color:#2f3a48;letter-spacing:.5px}
.menu{position:absolute;right:157px;top:0;display:flex;gap:38px;list-style:none;height:72px}
.menu li{font-size:12px;color:#6b6f75;line-height:72px;position:relative}
.menu li.active{color:var(--teal)}
.menu li.active::before{content:"";position:absolute;left:-8px;right:-8px;top:0;height:3px;background:var(--teal)}

/* hero */
.hero{top:108px;height:472px;background:linear-gradient(100deg,#6d5a49 0%,#a0896f 22%,#cfc1a8 40%,#8a7b6c 55%,#b49d87 72%,#d58b6a 88%,#7a5b4b 100%)}
.hero::after{content:"";position:absolute;inset:0;background:rgba(30,30,35,.25)}
.hero-copy{position:absolute;top:180px;z-index:1}
.hero h1{font-family:"Raleway",sans-serif;font-weight:800;font-size:29px;color:#fff;letter-spacing:.5px}
.hero p{font-weight:700;font-size:14px;color:#fff;margin-top:10px}
.btn{display:inline-block;background:var(--btn);color:#fff;font-family:"Open Sans",sans-serif;font-weight:700;font-size:11px;text-transform:uppercase;text-align:center;border-radius:2px}
.hero .btn{margin-top:22px;width:178px;height:40px;line-height:40px;font-size:12px}

/* section headings */
.heading{font-family:"Raleway",sans-serif;font-weight:700;font-size:21px;color:#2f3a48;letter-spacing:.5px}
.rule{width:102px;height:3px;background:var(--teal);margin:0 auto}
.lead{font-weight:700;font-size:13px;color:#2f3a48}

/* highlights */
.highlights{top:580px;height:664px;background:var(--light)}
.cards{position:absolute;left:157px;top:224px;width:886px;height:354px;display:flex;gap:2px}
.card{flex:1;background:#fff;border:1px solid #e6e6e6;text-align:center;padding-top:36px}
.card svg{width:40px;height:40px;fill:var(--teal)}
.card h3{font-weight:700;font-size:12px;color:#2f3a48;margin-top:10px}
.card p{font-size:11.5px;line-height:19px;color:var(--grey);width:160px;margin:18px auto 0}
.card .btn{margin-top:22px;width:106px;height:31px;line-height:31px;font-size:10px}

/* bands */
.band{height:155px;background:var(--teal)}
.band h2{position:absolute;left:157px;top:66px;font-family:"Raleway",sans-serif;font-weight:700;font-size:20px;color:#fff}
.band .ghost{position:absolute;height:42px;line-height:42px;background:var(--teal-dark);color:#fff;font-weight:700;font-size:11px;text-align:center;border-radius:2px;text-transform:uppercase}
.quote-band{top:1244px}
.sub-band{top:2739px}

/* services */
.services{top:1399px;height:412px;background:#fff}
.service-row{position:absolute;left:157px;top:226px;width:886px;display:flex}
.service{flex:1;text-align:center}
.service svg{width:18px;height:18px;fill:var(--teal)}
.service h3{font-weight:700;font-size:12px;color:#2f3a48;margin-top:6px}
.service p{font-size:11.5px;line-height:20px;color:var(--grey);width:190px;margin:12px auto 0}

/* testimonial */
.testimonial{top:1811px;height:410px;background:linear-gradient(180deg,#3a4352 0%,#2c3442 60%,#252c38 100%)}
.avatar{position:absolute;left:542px;top:79px;width:116px;height:116px;border-radius:50%;border:4px solid #fff;background:radial-gradient(circle at 50% 45%,#c9a48c 0%,#9b7c6b 50%,#dfe5ea 52%,#c7ced6 100%)}
.quote{position:absolute;top:214px;font-style:italic;font-weight:600;font-size:14.5px;line-height:27px;color:#e8ebef;letter-spacing:.3px}
.cite{position:absolute;top:282px;font-size:14px;color:#e8ebef}
.cite b{font-weight:700}
.dots{position:absolute;top:328px;left:581px;display:flex;gap:6px}
.dots span{width:9px;height:9px;border-radius:50%;border:1px solid #fff}
.dots span.on{background:#fff}

/* articles */
.articles{top:2221px;height:518px;background:#fff}
.thumb{position:absolute;top:259px;width:284px;height:186px}
.t1{left:157px;background:linear-gradient(135deg,#9ec6e6 0%,#3f82bd 45%,#0f3b6e 100%)}
.t2{left:458px;background:linear-gradient(160deg,#d7e6f2 0%,#8fb4d4 40%,#2f5878 100%)}
.t3{left:759px;background:linear-gradient(150deg,#b79b78 0%,#7a6552 45%,#d9d2c4 100%)}
.pager{position:absolute;right:157px;top:484px;display:flex;gap:4px;align-items:center}
.pager span{font-size:10px;color:var(--teal);height:18px;line-height:16px;padding:0 5px;border:1px solid var(--line)}
.pager span.on{background:var(--teal);color:#fff;border-color:var(--teal)}

/* partners */
.partners{top:2894px;height:361px;background:linear-gradient(120deg,#2d3543 0%,#3a4250 45%,#2a313d 100%)}
.partners .heading{color:#fff;position:absolute;top:84px;font-size:20px}
.partner-row{position:absolute;left:157px;top:198px;width:886px;display:flex;justify-content:space-between;align-items:center}
.partner{display:flex;align-items:center;gap:8px;font-family:"Open Sans",sans-serif;font-weight:700;font-size:21px;color:#fff}
.partner i{display:block;width:26px;height:26px;background:#fff}

/* footer */
footer{top:3255px;height:66px;background:#fff}
footer .copy{position:absolute;left:157px;top:26px;font-size:9px;color:var(--grey)}
footer .social{right:157px;top:22px}
.to-top{position:absolute;left:1107px;bottom:0;width:36px;height:20px;background:#343c48;border-radius:3px 3px 0 0}
.to-top svg{display:block;margin:5px auto 0}
</style>
</head>
<body>
<div class="page">

  <div class="topbar">
    <span class="note">Ardmoor Legal is Under Construction</span>
    <div class="social" aria-label="Social profiles"><span></span><span></span><span></span></div>
  </div>

  <header class="nav">
    <div class="brand">ARDMOOR LEGAL</div>
    <ul class="menu">
      <li class="active">Home</li><li>Who We Are</li><li>Our Services</li><li>Careers</li><li>Terms and Conditions</li><li>Articles</li><li>Contact</li>
    </ul>
  </header>

  <section class="hero" role="img" aria-label="Professionals walking through a sunlit glass office lobby">
    <div class="hero-copy center">
      <h1>ARDMOOR LEGAL</h1>
      <p>Nullam fringilla tristique elit id varius</p>
      <span class="btn">Let's Get Started</span>
    </div>
  </section>

  <section class="highlights">
    <h2 class="heading abs center" style="top:78px">OUR HIGHLIGHTS</h2>
    <div class="abs center" style="top:139px"><div class="rule"></div></div>
    <p class="lead abs center" style="top:181px">Nullam fringilla tristique elit id varius.</p>
    <div class="cards">
      <div class="card">
        <svg viewBox="0 0 40 40"><circle cx="20" cy="11" r="6"/><circle cx="9" cy="14" r="4.5"/><circle cx="31" cy="14" r="4.5"/><path d="M10 34c0-8 4-14 10-14s10 6 10 14z"/><path d="M1 31c0-6 3-10 8-10 2 0 3 .5 4 1-3 3-4 6-4 9z"/><path d="M39 31c0-6-3-10-8-10-2 0-3 .5-4 1 3 3 4 6 4 9z"/></svg>
        <h3>WHO WE ARE</h3>
        <p>Nullam fringilla tristique elit id varius. Nulla lacinia quam nec venenatis dignissim. Vivamus volutpat tempus semper. Cras feugiat mi sit amet risus consectetur.</p>
        <span class="btn">Learn More</span>
      </div>
      <div class="card">
        <svg viewBox="0 0 40 40"><path d="M10 4h24l-4 28H6z"/><path d="M6 34h24l-1 3H5z"/></svg>
        <h3>OUR EXPERTISE</h3>
        <p>Nullam fringilla tristique elit id varius. Nulla lacinia quam nec venenatis dignissim. Vivamus volutpat tempus semper. Cras feugiat mi sit amet risus consectetur.</p>
        <span class="btn">Learn More</span>
      </div>
      <div class="card">
        <svg viewBox="0 0 40 40"><path d="M14 8h12v5h-3v-2h-6v2h-3z"/><rect x="4" y="13" width="32" height="22" rx="3"/></svg>
        <h3>CAREERS</h3>
        <p>Nullam fringilla tristique elit id varius. Nulla lacinia quam nec venenatis dignissim. Vivamus volutpat tempus semper. Cras feugiat mi sit amet risus consectetur.</p>
        <span class="btn">Learn More</span>
      </div>
      <div class="card">
        <svg viewBox="0 0 40 40"><path d="M29 3l8 8-21 21-9 2 2-9z"/></svg>
        <h3>OUR ARTICLES</h3>
        <p>Nullam fringilla tristique elit id varius. Nulla lacinia quam nec venenatis dignissim. Vivamus volutpat tempus semper. Cras feugiat mi sit amet risus consectetur.</p>
        <span class="btn">Learn More</span>
      </div>
    </div>
  </section>

  <section class="band quote-band">
    <h2>NEED HELP WITH YOUR LEGAL ISSUE? REQUEST A QUOTATION.</h2>
    <span class="ghost" style="left:875px;top:56px;width:139px">Get A Quote</span>
  </section>

  <section class="services">
    <h2 class="heading abs center" style="top:80px">OUR SERVICES</h2>
    <div class="abs center" style="top:141px"><div class="rule"></div></div>
    <p class="lead abs center" style="top:183px">Nullam fringilla tristique elit id varius.</p>
    <div class="service-row">
      <div class="service">
        <svg viewBox="0 0 20 20"><path d="M10 2l9 8h-3v8h-4v-5H8v5H4v-8H1z"/></svg>
        <h3>PROPERTY &amp; WILLS</h3>
        <p>Nullam fringilla tristique elit id varius ipsum. Lorem lacinia quam nec venenatis sadips dignissim.</p>
      </div>
      <div class="service">
        <svg viewBox="0 0 20 20"><circle cx="10" cy="6" r="4"/><path d="M3 19c0-5 3-8 7-8s7 3 7 8z"/></svg>
        <h3>POWER OF ATTORNEY</h3>
        <p>Nullam fringilla tristique elit id varius ipsum. Lorem lacinia quam nec venenatis sadips dignissim.</p>
      </div>
      <div class="service">
        <svg viewBox="0 0 20 20"><circle cx="6" cy="7" r="4.5"/><path d="M9 9l9 8-2 2-2-2-1 1-2-2 1-1-4-4z"/></svg>
        <h3>PROBATE &amp; ESTATE</h3>
        <p>Nullam fringilla tristique elit id varius ipsum. Lorem lacinia quam nec venenatis sadips dignissim.</p>
      </div>
      <div class="service">
        <svg viewBox="0 0 20 20"><path d="M14 1l5 5-11 11-6 2 2-6z"/></svg>
        <h3>CONSULTANCY &amp; AGENCY</h3>
        <p>Nullam fringilla tristique elit id varius ipsum. Lorem lacinia quam nec venenatis sadips dignissim.</p>
      </div>
    </div>
  </section>

  <section class="testimonial" role="img" aria-label="Dimmed photograph of people crossing a busy office concourse">
    <div class="avatar" role="img" aria-label="Portrait of the senior partner"></div>
    <p class="quote center">“Nullam fringilla tristique elit id varius. Nulla lacinia quam nec venenatis dignissim. Vivamus volutpat tempus semper.<br>Cras feugiat mi sit amet risus consectetur.”</p>
    <p class="cite center"><b>Graham Pellow • Senior Partner</b>, Ardmoor Legal</p>
    <div class="dots"><span class="on"></span><span></span></div>
  </section>

  <section class="articles">
    <h2 class="heading abs center" style="top:99px">ARTICLES</h2>
    <div class="abs center" style="top:160px"><div class="rule"></div></div>
    <p class="lead abs center" style="top:212px">Nullam fringilla tristique elit id varius.</p>
    <div class="thumb t1" role="img" aria-label="Silhouettes of two professionals by an office window"></div>
    <div class="thumb t2" role="img" aria-label="Business people talking in front of a glass building"></div>
    <div class="thumb t3" role="img" aria-label="Colleagues reviewing a laptop at a meeting table"></div>
    <div class="pager"><span class="on">1</span><span>2</span><span style="border:none">Next ›</span></div>
  </section>

  <section class="band sub-band">
    <h2 style="top:68px">SUBSCRIBE TO OUR NEWSLETTER FOR THE LATEST NEWS</h2>
    <span class="ghost" style="left:881px;top:56px;width:129px">Subscribe</span>
  </section>

  <section class="partners" role="img" aria-label="Dimmed photograph of hands signing documents on a desk">
    <h2 class="heading center">VERIFIED PARTNERS</h2>
    <div class="partner-row">
      <span class="partner">Guides From Counsel</span>
      <span class="partner">Creature Foundation</span>
      <span class="partner">Dorvo</span>
      <span class="partner"><i></i>Malpeth</span>
      <span class="partner">Kel QR</span>
    </div>
  </section>

  <footer>
    <span class="copy">© Copyright 2017 - 2018 &nbsp;|&nbsp; All Rights Reserved &nbsp;|&nbsp; Ardmoor Legal</span>
    <div class="social" aria-label="Social profiles"><span></span><span></span><span></span></div>
    <div class="to-top"><svg width="12" height="8" viewBox="0 0 12 8"><path d="M1 7l5-5 5 5" stroke="#fff" stroke-width="2" fill="none"/></svg></div>
  </footer>

</div>
</body>
</html>
```